Business Card Design Project

An education/enrichment centre needs a business card for the directors and teachers. Attached is the logo. apart from the logo, the tact line "Growing Through Discovery" is needed to be shown in the card

```html
<!DOCTYPE html>
<html lang="en">
<head>
<meta charset="utf-8">
<title>Bright Grove Academy – Business Card</title>
<link rel="stylesheet" href="https://fonts.googleapis.com/css2?family=Montserrat:wght@600&family=Open+Sans:wght@400&family=Tinos&display=swap">
<style>
  :root {
    --page-bg: #2b2b2b;
    --card-white: #ffffff;
    --brand-blue: #3a4fa2;
    --band-light: #4d70bb;
    --band-dark: #3a51a3;
    --text-white: #ffffff;
    --text-dark: #1c1c1c;
  }
  * { margin: 0; padding: 0; box-sizing: border-box; }
  html, body {
    width: 1000px;
    height: 1200px;
    overflow: hidden;
    background: var(--page-bg);
  }
  .canvas {
    position: relative;
    width: 1000px;
    height: 1200px;
  }
  .business-card {
    position: absolute;
    left: 145px;
    top: 376px;
    width: 723px;
    height: 423px;
    background: var(--card-white);
    overflow: hidden;
  }
  .card-art {
    position: absolute;
    inset: 0;
  }
  .brand-name {
    position: absolute;
    left: 162px;
    width: 400px;
    top: 108px;
    text-align: center;
    font-family: "Montserrat", Arial, sans-serif;
    font-weight: 600;
    font-size: 28px;
    line-height: 1.25;
    letter-spacing: 3px;
    color: var(--brand-blue);
    text-transform: uppercase;
  }
  .tagline {
    position: absolute;
    left: 272px;
    width: 180px;
    top: 266px;
    text-align: center;
    font-family: "Open Sans", Arial, sans-serif;
    font-weight: 400;
    font-size: 17px;
    line-height: 1.3;
    color: var(--text-white);
  }
  .holder {
    position: absolute;
    right: 35px;
    top: 190px;
    text-align: right;
  }
  .holder-name {
    font-family: "Montserrat", Arial, sans-serif;
    font-weight: 600;
    font-size: 20px;
    letter-spacing: 0.3px;
    color: var(--brand-blue);
    text-transform: uppercase;
  }
  .holder-role {
    margin-top: 1px;
    font-family: "Tinos", "Times New Roman", serif;
    font-size: 16px;
    color: var(--text-dark);
  }
  .contact-list {
    position: absolute;
    list-style: none;
    font-family: "Open Sans", Arial, sans-serif;
    font-size: 15.5px;
    color: var(--text-white);
  }
  .contact-list li {
    display: flex;
    align-items: center;
    gap: 8px;
    height: 34px;
  }
  .contact-list--left { left: 35px; top: 282px; }
  .contact-list--right { right: 35px; top: 282px; }
  .contact-list--right li { justify-content: flex-end; }
  .contact-icon { width: 18px; height: 18px; flex: none; }
</style>
</head>
<body>
<main class="canvas">
  <article class="business-card">
    <svg class="card-art" width="723" height="423" viewBox="0 0 723 423" aria-hidden="true">
      <defs>
        <radialGradient id="bandGlow" cx="0.5" cy="0.45" r="0.6">
          <stop offset="0" stop-color="#4d70bb"/>
          <stop offset="1" stop-color="#3a51a3"/>
        </radialGradient>
      </defs>
      <rect class="top-panel" x="0" y="0" width="723" height="254" fill="#ffffff"/>
      <rect class="info-band" x="0" y="254" width="723" height="169" fill="url(#bandGlow)"/>
    </svg>

    <h1 class="brand-name">Bright Grove<br>Academy</h1>
    <p class="tagline">Growing Through<br>Discovery</p>

    <div class="holder">
      <p class="holder-name">Mara Ellis</p>
      <p class="holder-role">Directors</p>
    </div>

    <ul class="contact-list contact-list--left">
      <li>
        <svg class="contact-icon" viewBox="0 0 18 18" aria-hidden="true">
          <rect x="4" y="1" width="10" height="16" rx="1.5" fill="none" stroke="#fff" stroke-width="1.6"/>
          <line x1="4" y1="13" x2="14" y2="13" stroke="#fff" stroke-width="1.3"/>
          <circle cx="9" cy="15" r="0.9" fill="#fff"/>
        </svg>
        <span>+1 555 014 2280</span>
      </li>
      <li>
        <svg class="contact-icon" viewBox="0 0 18 18" aria-hidden="true">
          <rect x="1" y="4" width="16" height="11" fill="#fff"/>
          <polyline points="1,4 9,11 17,4" fill="none" stroke="#3a51a3" stroke-width="1.4"/>
        </svg>
        <span>hello@brightgroveacademy.com</span>
      </li>
    </ul>

    <ul class="contact-list contact-list--right">
      <li>
        <span>+1 555 014 2280</span>
        <svg class="contact-icon" viewBox="0 0 18 18" aria-hidden="true">
          <path d="M4 1.5l3 3-1.6 2.1c.9 2 2.4 3.5 4.4 4.4l2.1-1.6 3 3-1.8 2.6C8 15 3 10 1.4 3.3z" fill="none" stroke="#fff" stroke-width="1.5" stroke-linejoin="round"/>
        </svg>
      </li>
      <li>
        <span>www.brightgroveacademy.com</span>
        <svg class="contact-icon" viewBox="0 0 18 18" aria-hidden="true">
          <circle cx="9" cy="9" r="7.5" fill="none" stroke="#fff" stroke-width="1.5"/>
          <ellipse cx="9" cy="9" rx="3.2" ry="7.5" fill="none" stroke="#fff" stroke-width="1.2"/>
          <line x1="1.5" y1="9" x2="16.5" y2="9" stroke="#fff" stroke-width="1.2"/>
        </svg>
      </li>
    </ul>
  </article>
</main>
</body>
</html>
```